Flyer für einen Pflegedienst
Zielgruppe
Wir sind ein Pflegedienst, unsere Zielgruppe sind alle Menschen die Unterstützung brauchen. Das sind im Hauptteil Senioren.
Aufgabenstellung
Der Flyer soll im DIN A5 Format designed sein. Der Print soll hochwertig sein. Wir möchten vor allem wohlhabendere Kunden damit ansprechen. Er soll die Kunden direkt packen, aber auch nicht zu viele Informationen beinhalten, die einen überfordern.

```html
<!DOCTYPE html>
<html lang="de">
<head>
<meta charset="utf-8">
<title>Pflege Wendt – Flyer A5</title>
<link rel="stylesheet" href="https://fonts.googleapis.com/css2?family=Dancing+Script:wght@600&family=Lato:wght@400;700&display=swap">
<style>
  :root {
    --green: #0b7f36;
    --orange: #ee6a33;
    --pale: #d3e1db;
    --canvas: #c9d7d5;
    --white: #ffffff;
    --text: #5a5f5d;
    --script: "Dancing Script", cursive;
    --sans: "Lato", Arial, sans-serif;
  }
  * { box-sizing: border-box; margin: 0; padding: 0; }
  html, body { width: 900px; height: 1200px; overflow: hidden; }
  body { background: var(--canvas); font-family: var(--sans); position: relative; }

  .page {
    position: absolute; top: 310px; width: 410px; height: 580px;
    background: var(--white); overflow: hidden;
    box-shadow: 0 14px 30px rgba(40, 60, 58, 0.18);
  }
  .page--front { left: 25px; }
  .page--back { left: 465px; background: linear-gradient(#fff 60%, #eceff1 100%); }

  /* Front */
  .brand {
    position: absolute; top: 14px; left: 0; width: 100%;
    display: flex; justify-content: center; align-items: center; gap: 6px;
    font-family: var(--sans); font-weight: 700; font-size: 14px; color: var(--green);
    letter-spacing: 0.3px;
  }
  .brand__dot { width: 12px; height: 12px; border-radius: 50%; background: var(--green); }
  .front__band { position: absolute; left: 0; width: 100%; top: 106px; height: 94px; background: var(--pale); }
  .front__green { position: absolute; left: 0; width: 100%; top: 200px; height: 302px; background: var(--green); }
  .front__photo {
    position: absolute; top: 77px; left: 27px; width: 356px; height: 258px;
    background: linear-gradient(90deg, #7a4a2c 0%, #a47a5c 10%, #e9ebec 35%, #f3f4f5 60%, #dfe5e3 100%);
  }
  .front__headline {
    position: absolute; top: 365px; width: 100%; text-align: center;
    font-family: var(--script); font-weight: 600; font-size: 19px; line-height: 22px; color: var(--white);
  }
  .divider { height: 1px; width: 26px; background: rgba(255,255,255,0.55); }
  .divider--dark { background: #b8c7c1; }
  .front__divider { position: absolute; top: 418px; left: 192px; }
  .front__body {
    position: absolute; top: 438px; width: 100%; text-align: center;
    font-size: 7.2px; line-height: 12px; color: var(--white);
  }
  .front__footer {
    position: absolute; top: 502px; left: 0; width: 100%; height: 71px; background: var(--orange);
    color: var(--white); font-size: 6.6px; line-height: 11px; text-align: center; padding-top: 18px;
  }

  /* Back */
  .back__green { position: absolute; top: 0; left: 0; width: 100%; height: 268px; background: var(--green); }
  .back__title {
    position: absolute; top: 36px; left: 27px;
    font-family: var(--script); font-weight: 600; font-size: 18px; color: var(--white);
  }
  .back__divider { position: absolute; top: 66px; left: 27px; }
  .columns { position: absolute; left: 27px; width: 356px; display: flex; gap: 18px; }
  .columns p { flex: 1; font-size: 6.8px; line-height: 11px; }
  .back__intro { top: 84px; color: var(--white); }
  .back__photo {
    position: absolute; top: 125px; left: 27px; width: 356px; height: 143px;
    background: linear-gradient(100deg, #e7a9bd 0%, #d99a8a 35%, #c98a6c 55%, #5f8aa6 85%, #4d7b98 100%);
  }
  .hotline {
    position: absolute; top: 268px; left: 27px; width: 356px; height: 56px; background: var(--pale);
    text-align: center; color: var(--green);
  }
  .hotline__number { margin-top: 10px; font-size: 15px; font-weight: 400; letter-spacing: 0.2px; }
  .hotline__note { margin-top: 3px; font-size: 6.6px; }
  .back__about {
    position: absolute; top: 341px; left: 27px;
    font-family: var(--script); font-weight: 600; font-size: 13px; color: var(--green);
  }
  .back__about-divider { position: absolute; top: 366px; left: 27px; }
  .back__text { top: 383px; color: var(--text); }

  .services { position: absolute; top: 432px; left: 27px; width: 356px; display: grid; grid-template-columns: 1fr 1fr; column-gap: 18px; row-gap: 28px; }
  .service { display: flex; gap: 9px; }
  .service__tick { width: 13px; height: 13px; flex: none; margin-top: 1px; }
  .service__name { font-family: var(--script); font-weight: 600; font-size: 10px; color: var(--green); }
  .service__text { margin-top: 3px; font-size: 6.2px; line-height: 10px; color: var(--text); }
  .back__rule { position: absolute; bottom: 0; left: 0; width: 100%; height: 7px; background: var(--orange); }
</style>
</head>
<body>

<section class="page page--front">
  <div class="brand"><span class="brand__dot"></span>Pflege Wendt</div>
  <div class="front__band"></div>
  <div class="front__green"></div>
  <div class="front__photo" role="img" aria-label="Foto: ältere Dame mit Gehhilfe und lächelnde Pflegerin in weißer Kleidung auf einer hellen Terrasse"></div>
  <h1 class="front__headline">Pflege mit Herz<br>bei Ihnen zuhause</h1>
  <div class="divider front__divider"></div>
  <p class="front__body">Mit einem engagierten Team aus examiniertem Fachpersonal begleiten<br>wir unsere Patientinnen und Patienten einfühlsam durch den Alltag –<br>sicher, respektvoll und individuell.</p>
  <footer class="front__footer">
    Lindenallee 27, 45468 Mülheim an der Ruhr<br>
    info@pflege-wendt.de &nbsp;/&nbsp; www.pflege-wendt.de<br>
    0208 - 512 736 40 &nbsp;/&nbsp; 0208 – 512 736 49 (Fax)
  </footer>
</section>

<section class="page page--back">
  <div class="back__green"></div>
  <h2 class="back__title">Warum Sie uns Ihr Vertrauen schenken können</h2>
  <div class="divider back__divider"></div>
  <div class="columns back__intro">
    <p>Mit einem engagierten Team aus examiniertem Fachpersonal begleiten wir unsere Patientinnen</p>
    <p>und Patienten einfühlsam durch den Alltag – sicher, respektvoll und individuell.</p>
  </div>
  <div class="back__photo" role="img" aria-label="Foto: zwei Hände halten die Hand einer älteren Person in rosa Strickjacke"></div>
  <div class="hotline">
    <p class="hotline__number">0208 512 736 40</p>
    <p class="hotline__note">24/7 Rufbereitschaft</p>
  </div>
  <h3 class="back__about">Über uns</h3>
  <div class="divider divider--dark back__about-divider"></div>
  <div class="columns back__text">
    <p>Pellentesque interdum ac enim eu sagittis. Aenean rhoncus feugiat nibh id molestie.</p>
    <p>Duis pretium tortor in lacus porttitor lobortis. Praesent ipsum ex, pharetra non ullamcorper.</p>
  </div>
  <div class="services">
    <div class="service">
      <svg class="service__tick" viewBox="0 0 13 13"><rect x="0.6" y="0.6" width="11.8" height="11.8" fill="none" stroke="#ee6a33" stroke-width="1.2"/><path d="M3.3 6.6l2.3 2.3 4.2-4.6" fill="none" stroke="#ee6a33" stroke-width="1.2"/></svg>
      <div><p class="service__name">Behandlungspflege</p><p class="service__text">Aliquam dictum lacus vulputate magna aliquet faucibus amet sapien.</p></div>
    </div>
    <div class="service">
      <svg class="service__tick" viewBox="0 0 13 13"><rect x="0.6" y="0.6" width="11.8" height="11.8" fill="none" stroke="#ee6a33" stroke-width="1.2"/><path d="M3.3 6.6l2.3 2.3 4.2-4.6" fill="none" stroke="#ee6a33" stroke-width="1.2"/></svg>
      <div><p class="service__name">Grundpflege</p><p class="service__text">Aliquam dictum lacus vulputate magna aliquet faucibus amet sapien.</p></div>
    </div>
    <div class="service">
      <svg class="service__tick" viewBox="0 0 13 13"><rect x="0.6" y="0.6" width="11.8" height="11.8" fill="none" stroke="#ee6a33" stroke-width="1.2"/><path d="M3.3 6.6l2.3 2.3 4.2-4.6" fill="none" stroke="#ee6a33" stroke-width="1.2"/></svg>
      <div><p class="service__name">Betreuung</p><p class="service__text">Aliquam dictum lacus vulputate magna aliquet faucibus amet sapien.</p></div>
    </div>
    <div class="service">
      <svg class="service__tick" viewBox="0 0 13 13"><rect x="0.6" y="0.6" width="11.8" height="11.8" fill="none" stroke="#ee6a33" stroke-width="1.2"/><path d="M3.3 6.6l2.3 2.3 4.2-4.6" fill="none" stroke="#ee6a33" stroke-width="1.2"/></svg>
      <div><p class="service__name">Individuelle Beratung</p><p class="service__text">Aliquam dictum lacus vulputate magna aliquet faucibus amet sapien.</p></div>
    </div>
  </div>
  <div class="back__rule"></div>
</section>

</body>
</html>
```